The Q Collective Business Cards

We need a sleek looking business card for our real estate company. Looking for a clean, modern, eye catching design on a standard size business card.
Updates

Target Market(s)

General Public/Real Estate Clients

Industry/Entity Type

Real Estate

Contact Information for Business Card

Cards will be customized for each agent.

Colors

Designer to choose only greyscale colors for use in the design.

Requirements
Must have
• Black, white, gray color pallet, Photo area for headshot on the front of the card

```html
<!DOCTYPE html>
<html lang="en">
<head>
<meta charset="utf-8">
<title>The Q Collective – Business Card</title>
<link href="https://fonts.googleapis.com/css2?family=Alike&family=Mulish:wght@400;600&family=Poppins:wght@500;600&display=swap" rel="stylesheet">
<style>
  :root {
    --page: #2b2b2d;
    --card-back: #e6e7e9;
    --card-front: #f7f8fa;
    --ink: #1d1b1c;
    --ink-soft: #4a4a4e;
    --muted: #8a8b90;
    --swoosh: #c9cacd;
    --band: #231f20;
    --on-band: #ffffff;
    --photo-a: #d9d4cf;
    --photo-b: #6a5d52;
  }
  * { box-sizing: border-box; margin: 0; padding: 0; }
  html, body { width: 1200px; height: 976px; overflow: hidden; }
  body {
    background: var(--page);
    display: flex;
    flex-direction: column;
    align-items: center;
    justify-content: center;
    gap: 44px;
    font-family: "Mulish", sans-serif;
  }
  .card {
    position: relative;
    width: 585px;
    height: 360px;
    overflow: hidden;
    box-shadow: 0 10px 24px rgba(0,0,0,.45);
  }
  /* back side */
  .card--back {
    background: var(--card-back);
    display: flex;
    align-items: center;
    justify-content: center;
    gap: 18px;
  }
  .brand-square {
    width: 26px; height: 26px;
    background: var(--ink);
  }
  .brand-name {
    font-family: "Alike", serif;
    font-size: 44px;
    font-weight: 400;
    color: var(--ink);
    letter-spacing: .5px;
  }
  /* front side */
  .card--front { background: var(--card-front); }
  .card__art { position: absolute; inset: 0; z-index: 2; }
  .headshot {
    position: absolute;
    left: 40px; top: 112px;
    width: 270px; height: 248px;
    background: linear-gradient(160deg, var(--photo-a) 0%, #a8998c 45%, var(--photo-b) 100%);
  }
  .agent {
    position: absolute;
    left: 340px; top: 52px;
  }
  .agent__name {
    font-family: "Alike", serif;
    font-size: 34px;
    font-weight: 400;
    color: var(--ink-soft);
    line-height: 1;
  }
  .agent__title {
    font-size: 11px;
    color: var(--muted);
    margin-top: 6px;
  }
  .contacts {
    position: absolute;
    left: 340px; top: 128px;
    list-style: none;
    font-size: 11.5px;
    color: var(--muted);
  }
  .contacts li {
    display: flex;
    align-items: flex-start;
    gap: 10px;
    line-height: 1.5;
  }
  .contacts li + li.group { margin-top: 10px; }
  .contacts svg { width: 12px; height: 12px; margin-top: 3px; flex: none; fill: var(--ink); }
</style>
</head>
<body>

<section class="card card--back" aria-label="Card back">
  <span class="brand-square"></span>
  <span class="brand-name">The Q Collective</span>
</section>

<section class="card card--front" aria-label="Card front">
  <div class="headshot" role="img" aria-label="Agent headshot photo"></div>

  <div class="agent">
    <h1 class="agent__name">Ethan Marlow</h1>
    <p class="agent__title">Real Estate Agent/Broker</p>
  </div>

  <ul class="contacts">
    <li><svg viewBox="0 0 24 24"><path d="M6.6 10.8a15 15 0 0 0 6.6 6.6l2.2-2.2a1 1 0 0 1 1-.25 11.4 11.4 0 0 0 3.6.57 1 1 0 0 1 1 1V20a1 1 0 0 1-1 1A17 17 0 0 1 3 4a1 1 0 0 1 1-1h3.5a1 1 0 0 1 1 1c0 1.25.2 2.45.57 3.57a1 1 0 0 1-.25 1z"/></svg>555.014.0255</li>
    <li><svg viewBox="0 0 24 24"><path d="M5 3h10v4h4v14H5zM8 10h2v2H8zm4 0h2v2h-2zm-4 4h2v2H8zm4 0h2v2h-2z"/></svg>555.014.1234</li>
    <li class="group"><svg viewBox="0 0 24 24"><path d="M2 5h20v14H2zm2 2v.5l8 5 8-5V7l-8 5z"/></svg>info@theqcollective.com</li>
    <li><svg viewBox="0 0 24 24"><circle cx="12" cy="12" r="10"/></svg>www.theqcollective.com</li>
    <li class="group"><svg viewBox="0 0 24 24"><path d="M12 2a7 7 0 0 1 7 7c0 5-7 13-7 13S5 14 5 9a7 7 0 0 1 7-7zm0 4.5A2.5 2.5 0 1 0 12 11.5 2.5 2.5 0 0 0 12 6.5z"/></svg><span>8 Harbor Lane, Palm Shore<br>FL 30417</span></li>
  </ul>

  <svg class="card__art" viewBox="0 0 585 360" aria-hidden="true">
    <path d="M150 360 C310 300 460 245 585 198 L585 222 C480 262 340 315 245 360 Z" fill="var(--swoosh)"/>
    <path d="M245 360 C340 315 480 262 585 222 L585 360 Z" fill="var(--band)"/>
    <text x="302" y="352" transform="rotate(-22 302 352)" font-family="Poppins, sans-serif" font-weight="500" font-size="11" fill="var(--on-band)" textLength="262" lengthAdjust="spacingAndGlyphs">THE Q COLLECTIVE - REAL ESTATE TEAM</text>
  </svg>
</section>

</body>
</html>
```